HTML Web layout / data visualization for an information software application

We have a product used by patent analysts to allow them examine information stored in patents - particularly those patents that include biological sequences like DNA, RNA, and protein.

When the user opens up a particular patent, they currently see a very poorly organized wall of text, presenting fields of data to them in unorganized ways. We have attached screenshots of the current interface.

The project is to redesign that layout so that the same information is presented in a way which is brings important data to the the eyes of the user, categorizes data appropriately, and is visually appealing. We have proposed logical categorizations of data in the document called "Fields documentation."

The deliverable should be an HTML5 file that renders one or more of the examples of records we've provided in your new design.

Description of files:

"Examples of records badly displayed": MS Word file that shows three different examples of the records we would like to better visualize.

"screengrab1.tiff" and "screengrab2.tiff": pictures of how these records sit inside of our product. This is presented to give you a sense of screen real estate, our look and feel, and colors. We do not want the whole screen redesigned - just the record display itself.

"Fields documentation": detailed documentation of what each field means. We have tried to group them logically for you, and have also attempted to inform you as to which fields are linked to others.

Hi all,

Thanks for the designs so far. Unfortunately, nearly every design fails to understand the nature of the project. The problem we have is not about fonts and colors (although those matter). It is about grouping information together and displaying data in a way that provides insight. In the original brief, we say:

The document we have uploaded called "Fields documentation" is the most important document. We sense that very few of you have taken it into account. It provides notes on the nature of the data in the report and gives signs of the ways in which a creative designer might help to arrange the content.

Thanks for your consideration of this project.

TM

Target Market(s)

Patent analysts, heavily educated scientists, Ph.Ds.

Industry/Entity Type

Software

```html
<!DOCTYPE html>
<html lang="en">
<head>
<meta charset="utf-8">
<title>SeqLedger – Full aln results of workflow BRAF IP</title>
<link href="https://fonts.googleapis.com/css2?family=Arimo:ital,wght@0,400;0,700;1,400&display=swap" rel="stylesheet">
<style>
:root{
  --chrome-top:#ececec;
  --chrome-bottom:#d2d2d2;
  --chrome-line:#a9a9a9;
  --ink:#111;
  --ink-soft:#555;
  --sky:#cfe7f3;
  --sky-deep:#1f8cc9;
  --rail:#2a8fcb;
  --white:#fff;
  --tab-line:#9fb7c4;
}
*{box-sizing:border-box;margin:0;padding:0}
html,body{width:1200px;height:873px;overflow:hidden;background:var(--white)}
body{font-family:"Arimo",Arial,sans-serif;color:var(--ink)}
.stage{width:792px;height:576px;position:relative;transform:scale(1.5152,1.5156);transform-origin:0 0;overflow:hidden;background:var(--sky)}
.abs{position:absolute}

/* window chrome */
.titlebar{left:0;top:0;width:792px;height:20px;background:linear-gradient(var(--chrome-top),#dcdcdc);border-bottom:1px solid #bdbdbd;font-size:12.5px;text-align:center;line-height:20px;color:#333}
.lights{left:6px;top:4px;display:flex;gap:6px}
.lights span{width:12px;height:12px;border-radius:50%;background:#cfcfcf;border:1px solid #a7a7a7}
.toolbar{left:0;top:20px;width:792px;height:26px;background:linear-gradient(#dedede,var(--chrome-bottom))}
.navbtns{left:4px;top:4px;width:44px;height:18px;border:1px solid var(--chrome-line);border-radius:3px;background:#f3f3f3;display:flex}
.navbtns span{flex:1;font-size:9px;color:#888;text-align:center;line-height:16px}
.navbtns span+span{border-left:1px solid var(--chrome-line)}
.addtab{left:60px;top:4px;font-size:16px;color:#666;line-height:16px}
.urlbar{left:80px;top:3px;width:706px;height:20px;background:var(--white);border:1px solid var(--chrome-line);border-radius:3px;font-size:12.5px;line-height:18px;padding-left:24px}
.urlbar .site-dot{position:absolute;left:6px;top:3px;width:12px;height:12px;border-radius:50%;background:var(--sky-deep)}
.bookmarks{left:0;top:46px;width:792px;height:22px;background:linear-gradient(#d6d6d6,#c8c8c8);border-bottom:1px solid #9a9a9a;font-size:11.5px;font-weight:700;color:#444;line-height:22px}
.bookmarks ul{list-style:none;display:flex;gap:14px;position:absolute;left:97px}
.bm-icons{left:6px;top:6px;display:flex;gap:10px}
.bm-icons i{display:block;width:14px;height:10px;border:1.5px solid #555;border-radius:2px}

/* tabs */
.tab{top:90px;height:23px;border:1px solid var(--tab-line);border-bottom:none;background:#eef6fa;font-size:12px;line-height:22px;text-align:center;border-radius:2px 2px 0 0}
.tab.is-active{background:var(--white);height:24px}
.panel{left:4px;top:112px;width:781px;height:470px;background:var(--white);border-top:1px solid var(--tab-line)}

/* record header */
.hint{left:437px;top:117px;font-size:8px;font-style:italic}
.record-head{left:28px;top:128px;width:732px;height:48px;background:var(--sky)}
.head-label{font-size:11px;font-weight:700;left:10px}
.head-value{font-size:11px;left:77px}
.timeline{left:0;top:0;width:732px;height:48px}
.tl-tag{font-size:7.5px;text-align:center;line-height:9px;width:60px;margin-left:-30px}
.tl-year{font-size:11px;top:35px}

/* side nav */
.rail{left:126px;top:210px;width:2px;height:249px;background:var(--rail)}
.nav-item{width:110px;left:6px;text-align:right;font-size:11.5px}
.nav-item.is-current{font-weight:700;color:var(--ink)}
.nav-dot{left:124px;width:6px;height:6px;border-radius:50%;background:var(--rail)}
.nav-current-mark{left:120px;top:284px;width:14px;height:14px;border-radius:50%;border:2px solid var(--rail);background:var(--white)}

/* record body */
.record-title{left:176px;top:204px;font-size:11px;font-weight:700;line-height:13px;letter-spacing:.1px}
.field-label{left:176px;font-size:11.5px;font-weight:700}
.field-value{left:332px;font-size:11.5px;line-height:14px;width:400px}
.premium-note{left:532px;top:325px;font-size:7.5px;font-style:italic}
.footer-stub{left:18px;top:572px;width:130px;height:6px;background:#e3e3e3}
</style>
</head>
<body>
<div class="stage">
  <header class="abs titlebar">
    <div class="abs lights"><span></span><span></span><span></span></div>
    SeqLedger – Full aln results of workflow BRAF IP
  </header>
  <div class="abs toolbar">
    <div class="abs navbtns"><span>◀</span><span>▶</span></div>
    <div class="abs addtab">+</div>
    <div class="abs urlbar"><span class="site-dot"></span>https://my.seqledger.example/query?do=tmresult&amp;db=wf:2178462.resdb&amp;is_workspace_recognized=1&amp;</div>
  </div>
  <nav class="abs bookmarks">
    <div class="abs bm-icons"><i></i><i></i><i></i></div>
    <ul><li>Cadence Row ▾</li><li>News (85) ▾</li><li>Grants ▾</li><li>Web Favorites ▾</li><li>Orchard</li><li>.Home</li><li>Riverstore</li><li>BidHall</li><li>Yodel!</li><li>Orchard (32) ▾</li></ul>
  </nav>

  <div class="abs tab" style="left:8px;width:73px">Alignment</div>
  <div class="abs tab is-active" style="left:84px;width:121px">Subject Annotation</div>
  <div class="abs tab" style="left:208px;width:111px">Subject Sequence</div>
  <div class="abs tab" style="left:322px;width:109px">Query Sequence</div>
  <main class="abs panel"></main>

  <div class="abs hint">Mouse over blue dots to get exact date</div>
  <section class="abs record-head">
    <div class="abs head-label" style="top:3px">PN:</div><div class="abs head-value" style="top:3px">EP2021499</div>
    <div class="abs head-label" style="top:18px">Assignee:</div><div class="abs head-value" style="top:18px">Halden Institute</div>
    <div class="abs head-label" style="top:33px">Family:</div><div class="abs head-value" style="top:33px">EP2021499</div>
    <svg class="abs timeline" viewBox="0 0 732 48" aria-hidden="true">
      <line x1="262" y1="31" x2="712" y2="31" stroke="#000" stroke-width="3"/>
      <g fill="#2a8fcb">
        <circle cx="312" cy="31" r="6"/><circle cx="384" cy="31" r="6"/>
        <circle cx="564" cy="31" r="6"/><circle cx="585" cy="31" r="6"/><circle cx="672" cy="31" r="6"/>
      </g>
      <g stroke="#2a8fcb" stroke-width="1"><line x1="312" y1="24" x2="312" y2="19"/><line x1="384" y1="24" x2="384" y2="19"/><line x1="555" y1="20" x2="564" y2="27"/><line x1="585" y1="24" x2="585" y2="19"/><line x1="672" y1="24" x2="672" y2="19"/></g>
    </svg>
    <div class="abs tl-tag" style="left:312px;top:4px">Earliest<br>priority</div>
    <div class="abs tl-tag" style="left:384px;top:4px">Patent<br>filing</div>
    <div class="abs tl-tag" style="left:504px;top:4px">Earliest<br>publication</div>
    <div class="abs tl-tag" style="left:563px;top:4px">Publication<br>date</div>
    <div class="abs tl-tag" style="left:613px;top:6px">Entry<br>date</div>
    <div class="abs tl-tag" style="left:672px;top:4px">PCT<br>publication</div>
    <div class="abs tl-year" style="left:251px">2005</div><div class="abs tl-year" style="left:323px">2006</div>
    <div class="abs tl-year" style="left:396px">2007</div><div class="abs tl-year" style="left:469px">2008</div>
    <div class="abs tl-year" style="left:540px">2009</div><div class="abs tl-year" style="left:612px">2010</div>
    <div class="abs tl-year" style="left:684px">2011</div>
  </section>

  <div class="abs rail"></div>
  <div class="abs nav-item" style="top:213px">Invention</div><div class="abs nav-dot" style="top:218px"></div>
  <div class="abs nav-item" style="top:249px">Identifiers</div><div class="abs nav-dot" style="top:253px"></div>
  <div class="abs nav-item is-current" style="top:284px">Status &amp; priority</div><div class="abs nav-current-mark"></div>
  <div class="abs nav-item" style="top:320px">Sequence</div><div class="abs nav-dot" style="top:324px"></div>
  <div class="abs nav-item" style="top:355px">Claims</div><div class="abs nav-dot" style="top:359px"></div>
  <div class="abs nav-item" style="top:390px">Miscellaneous</div><div class="abs nav-dot" style="top:394px"></div>

  <h1 class="abs record-title">FUNCTIONAL ARRAYS FOR HIGH THROUGHPUT CHARACTERIZATION OF GENE<br>EXPRESSION REGULATORY ELEMENTS</h1>

  <div class="abs field-label" style="top:253px">Legal status</div>
  <div class="abs field-value" style="top:253px">Application</div>
  <div class="abs field-label" style="top:280px">Detailed legal status</div>
  <div class="abs field-value" style="top:280px">International application published with international search report;<br>2012-05-18</div>
  <div class="abs field-label" style="top:320px">Extended legal status</div>
  <div class="abs field-value" style="top:320px">PENDING</div>
  <div class="abs field-label" style="top:348px">National phase status</div>
  <div class="abs field-value" style="top:348px">AU=PENDING, EP=PENDING</div>
  <div class="abs premium-note">Only available for premium offerings</div>
  <svg class="abs" style="left:0;top:0" width="792" height="576" aria-hidden="true">
    <g stroke="#2a8fcb" stroke-width="1"><line x1="403" y1="326" x2="513" y2="333"/><line x1="500" y1="352" x2="532" y2="336"/></g>
  </svg>
  <div class="abs field-label" style="top:402px">Priority info</div>
  <div class="abs field-value" style="top:402px">20101112 US20100412862P; 20101220 US201061425174P; 20110728<br>US201161512754P</div>
  <div class="abs field-label" style="top:443px">Earliest priority number</div>
  <div class="abs field-value" style="top:443px">US20100412862P</div>

  <div class="abs footer-stub"></div>
</div>
</body>
</html>
```